Business Card Design Project

Business card for law firm
Use existing logo
Must have:
Gerald P. Whitcombe
2715-C West 6th
McAllen, TX 78521
gwhitcombe@dvlegalgroup.com
www.dvlegalgroup.com
956-412-3095

Target Market(s)

Clients and potential clients, generally adult, business background

Industry/Entity Type

Business

Requirements
Must have
• Our logo, see below

```html
<!DOCTYPE html>
<html lang="en">
<head>
<meta charset="utf-8">
<title>Davenport Vale – Business Card</title>
<link rel="stylesheet" href="https://fonts.googleapis.com/css2?family=Marcellus+SC&family=Lato:wght@400;700&display=swap">
<style>
  :root {
    --page-bg: #e6e6e8;
    --card-border: #2b2b2d;
    --card-face: #fbfbfb;
    --ink-dark: #1f1f1f;
    --ink-mid: #555555;
    --ink-accent: #6f8487;
    --band: #4a4a4a;
    --rule: #8a8a8a;
  }
  * { margin: 0; padding: 0; box-sizing: border-box; }
  html, body { width: 1200px; height: 1000px; overflow: hidden; }
  body { background: var(--page-bg); position: relative; }

  .business-card {
    position: absolute; left: 100px; top: 214px;
    width: 1000px; height: 572px;
    background: var(--card-border);
    padding: 24px;
    box-shadow: 0 18px 40px rgba(0,0,0,0.25);
  }
  .card-face {
    position: relative; width: 100%; height: 100%;
    background: var(--card-face);
    overflow: hidden;
  }

  .firm-mark {
    position: absolute; left: 40px; top: 38px;
    width: 58px; height: 58px; background: var(--ink-dark);
  }
  .firm-name {
    position: absolute; left: 114px; top: 36px;
    font-family: "Marcellus SC", serif; font-size: 52px; line-height: 1;
    color: var(--ink-dark); letter-spacing: 1px;
  }
  .firm-rule {
    position: absolute; left: 114px; top: 98px; width: 500px;
    border-top: 1.5px solid var(--rule);
  }
  .firm-tagline {
    position: absolute; left: 116px; top: 104px;
    font-family: "Marcellus SC", serif; font-size: 24px;
    color: var(--ink-accent); letter-spacing: 1px;
  }
  .header-rule {
    position: absolute; left: 40px; right: 40px; top: 182px;
    border-top: 1px solid var(--rule);
  }

  .attorney {
    position: absolute; right: 62px; top: 218px; text-align: right;
    font-family: "Marcellus SC", serif; color: var(--ink-dark);
  }
  .attorney-name { font-size: 40px; line-height: 1.1; color: var(--ink-mid); }
  .attorney-name strong { color: var(--ink-dark); font-weight: 400; }
  .attorney-title { font-size: 26px; margin-top: 4px; }
  .attorney-bar {
    position: absolute; right: 40px; top: 222px;
    width: 6px; height: 80px; background: var(--ink-dark);
  }

  .contact-band { position: absolute; left: 0; top: 320px; }

  .contact {
    position: absolute; top: 420px;
    font-family: "Lato", sans-serif; font-weight: 700;
    font-size: 21px; line-height: 1.35; color: var(--ink-dark);
  }
  .contact-address { left: 70px; }
  .contact-phone { left: 420px; width: 200px; text-align: center; }
  .contact-web { right: 50px; text-align: right; }
</style>
</head>
<body>
  <div class="business-card">
    <div class="card-face">
      <div class="firm-mark"></div>
      <div class="firm-name">Davenport Vale</div>
      <div class="firm-rule"></div>
      <div class="firm-tagline">Attorneys and Counselors</div>
      <div class="header-rule"></div>

      <div class="attorney">
        <div class="attorney-name">Gerald <strong>P. Whitcombe</strong></div>
        <div class="attorney-title">Attorney of Law</div>
      </div>
      <div class="attorney-bar"></div>

      <svg class="contact-band" width="952" height="100" viewBox="0 0 952 100">
        <line x1="0" y1="26" x2="952" y2="26" stroke="#4a4a4a" stroke-width="2"/>
        <rect x="0" y="36" width="952" height="22" fill="#4a4a4a"/>
        <line x1="0" y1="68" x2="952" y2="68" stroke="#4a4a4a" stroke-width="2"/>

        <g class="icon-home" transform="translate(150 47)">
          <circle r="38" fill="#4a4a4a" stroke="#fbfbfb" stroke-width="3"/>
          <path d="M-18 2 L0 -16 L18 2" fill="none" stroke="#fff" stroke-width="4" stroke-linejoin="round"/>
          <path d="M-12 0 V16 H-3 V6 H3 V16 H12 V0" fill="#fff"/>
        </g>

        <g class="icon-phone" transform="translate(520 47)">
          <circle r="38" fill="#4a4a4a" stroke="#fbfbfb" stroke-width="3"/>
          <path d="M-18 -6 Q0 -18 18 -6 L14 0 L7 -3 L7 -7 Q0 -10 -7 -7 L-7 -3 L-14 0 Z" fill="#fff"/>
          <rect x="-12" y="0" width="24" height="16" rx="3" fill="#fff"/>
          <circle cy="8" r="4" fill="#4a4a4a"/>
        </g>

        <g class="icon-globe" transform="translate(830 47)">
          <circle r="38" fill="#4a4a4a" stroke="#fbfbfb" stroke-width="3"/>
          <g fill="none" stroke="#fff" stroke-width="2.5">
            <circle r="17"/>
            <ellipse rx="7" ry="17"/>
            <line x1="-17" y1="0" x2="17" y2="0"/>
            <path d="M-14 -9 H14 M-14 9 H14"/>
          </g>
        </g>
      </svg>

      <div class="contact contact-address">2715-C West 6th<br>McAllen, TX 78521</div>
      <div class="contact contact-phone">956-412-3095</div>
      <div class="contact contact-web">gwhitcombe@dvlegalgroup.com<br>www.dvlegalgroup.com</div>
    </div>
  </div>
</body>
</html>
```